Stationary for Beauty and Spa School

Create a business card, letterhead and envelopes (primarily #10 envelope with and without window and catalog envelope) for a beauty and wellness school in Miami, Fl. We offer 8 different programs of study and need an eye catching look. Looking for a combination of modern yet sophisticated. Nothing corporate or business looking. Would like to have a look and feel that is similar (or incorporates aspects) of a new website we will be launching in the next 30 days (screen shot attached.)

The final design should communicate style and elegance in a down to earth and friendly way. We strive to provide our students with quality education, friendly and amicable staff and experienced instructors.
Updates

Hello. FYI, in order to print an aesthetically appealing business card, we would like to print them (the business cards) using silk printing method, with spot UV coating (on some elements, maybe the logo, or depending on the design) and die cuts. Please think of this when preparing your design.

Only 1 day left, please submit your designs for selection. Thanks

Target Market(s)

Adults 18-49 years who are mostly interested in beauty and fashion. Need a youthful & modern look, yet sophisticated and elegant.

Industry/Entity Type

School

Colors
e34197
6b449b
add136
f79021

Requirements
Must have
• Similar look and feel as website (see attached screen shot)
Same look and feel of website (see attached screenshot)
Logo
Address: 5126 NW 14th Avenue. Miami, Fl 33157
Telephone: 305-914-3062
Fax: 786-552-4190
website/url: www.lumaroveacademy.edu
incorporate Photo of blonde model (attached)
Nice to have
• Tag line: "Beautify your future." Also, maybe two-sided business card. Would be nice if we could mention our programs (maybe in the back of the card). Below are the program offerings (names cannot be changed but order is irrelevant)... Cosmetology, Barber, Spa Therapy, Massage Therapy, Makeup Artistry, Skin Care, Manicure, Pedicure & Nail Extensions, Full Specialist.

A design with text plus a beautiful photo of a model is appealing. Attached to the files is a sample of a cover for a student handbook we have created. You should use the photo of the blonde model (attached) in your design. The original (quality) version of this stock photograph has been uploaded.

Also would be nice to request clients to follow us on facebook and instagram by including the icons.
Should not have
• A corporate or business look. We are a vocational school teaching beauty and spa programs and we like our advertising to have a look that resembles the industry. We do not want a very serious look or snobby feel.

```html
<!DOCTYPE html>
<html lang="en">
<head>
<meta charset="utf-8">
<title>Lumarove Academy of Beauty – Business Card</title>
<link rel="stylesheet" href="https://fonts.googleapis.com/css2?family=Open+Sans:wght@400;600;700&display=swap">
<style>
  :root {
    --backdrop: #ece8e4;
    --card-white: #ffffff;
    --brand-purple: #7b24c2;
    --stripe-dark: #2b2b2e;
    --ink: #1d1d1f;
    --tagline-blue: #1f4f8a;
    --text-on-purple: #ffffff;
    --card-shadow: rgba(0, 0, 0, 0.22);
  }
  * { margin: 0; padding: 0; box-sizing: border-box; }
  html, body { width: 1200px; height: 720px; overflow: hidden; }
  body {
    background: var(--backdrop);
    font-family: "Open Sans", Arial, sans-serif;
    position: relative;
  }
  .card {
    position: absolute;
    width: 560px;
    height: 320px;
    box-shadow: 0 8px 22px var(--card-shadow);
    overflow: hidden;
  }

  /* Front side */
  .card--front { left: 50px; top: 70px; background: var(--card-white); color: var(--ink); }
  .front-stripe { position: absolute; left: 0; top: 0; width: 40px; height: 320px; }
  .front-logo { position: absolute; left: 64px; top: 42px; }
  .brand-name {
    font-size: 54px; font-weight: 700; line-height: 1; letter-spacing: -1px;
    color: var(--ink); display: flex; align-items: center; gap: 12px;
  }
  .brand-dot { width: 16px; height: 16px; border-radius: 50%; background: var(--brand-purple); }
  .brand-sub { font-size: 15px; font-weight: 600; letter-spacing: 0.5px; margin: 6px 0 0 30px; }
  .address {
    position: absolute; right: 28px; top: 132px; text-align: right;
    font-size: 12px; line-height: 1.35;
  }
  .tagline {
    position: absolute; left: 56px; top: 170px;
    font-size: 17px; font-weight: 600; color: var(--tagline-blue);
  }
  .contact-list { position: absolute; left: 58px; top: 200px; list-style: none; font-size: 12.5px; }
  .contact-list li { display: flex; align-items: center; gap: 9px; height: 20px; }
  .contact-icon { width: 12px; height: 12px; flex: none; }

  /* Back side */
  .card--back {
    left: 610px; top: 340px; background: var(--brand-purple);
    color: var(--text-on-purple); text-align: center;
  }
  .back-logo { margin-top: 46px; }
  .back-logo .brand-name { color: var(--text-on-purple); justify-content: center; font-size: 50px; }
  .back-logo .brand-dot { background: var(--text-on-purple); }
  .back-logo .brand-sub { margin: 6px 0 0 0; font-size: 14px; }
  .offerings-title { margin-top: 16px; font-size: 19px; font-weight: 700; }
  .program-lines { list-style: none; margin-top: 6px; font-size: 14px; line-height: 1.45; }
</style>
</head>
<body>

<section class="card card--front" aria-label="Business card front">
  <svg class="front-stripe" viewBox="0 0 40 320" aria-hidden="true">
    <polygon points="0,60 22,60 22,175 0,175" fill="var(--brand-purple)"/>
    <polygon points="0,175 22,175 22,320 0,320" fill="var(--stripe-dark)"/>
    <polygon points="22,60 30,60 30,175 22,175" fill="#9b59d6"/>
  </svg>

  <div class="front-logo">
    <div class="brand-name"><span class="brand-dot"></span>Lumarove</div>
    <div class="brand-sub">ACADEMY OF BEAUTY</div>
  </div>

  <address class="address" style="font-style:normal">
    5126 NW 14th Avenue<br>Miami, Fl 33157
  </address>

  <p class="tagline">Beautify Your Future</p>

  <ul class="contact-list">
    <li>
      <svg class="contact-icon" viewBox="0 0 12 12" aria-hidden="true"><circle cx="6" cy="6" r="5.5" fill="none" stroke="var(--ink)"/><path d="M4 3.2c-.6.5-.6 1.8.6 3.2s2.6 1.8 3.2 1.2l-.9-1-.8.4c-.6-.3-1.3-1-1.6-1.6l.4-.8z" fill="var(--ink)"/></svg>
      305-914-3062
    </li>
    <li>
      <svg class="contact-icon" viewBox="0 0 12 12" aria-hidden="true"><rect x="1" y="4" width="10" height="7" rx="1" fill="var(--ink)"/><rect x="3" y="1" width="6" height="4" fill="none" stroke="var(--ink)"/></svg>
      786-552-4190
    </li>
    <li>
      <svg class="contact-icon" viewBox="0 0 12 12" aria-hidden="true"><circle cx="6" cy="6" r="5.2" fill="none" stroke="var(--ink)"/><ellipse cx="6" cy="6" rx="2.2" ry="5.2" fill="none" stroke="var(--ink)"/><line x1="0.8" y1="6" x2="11.2" y2="6" stroke="var(--ink)"/></svg>
      www.lumaroveacademy.edu
    </li>
    <li>
      <svg class="contact-icon" viewBox="0 0 12 12" aria-hidden="true"><rect x="0.5" y="0.5" width="11" height="11" rx="2" fill="var(--stripe-dark)"/></svg>
      /lumaroveacademy
    </li>
    <li>
      <svg class="contact-icon" viewBox="0 0 12 12" aria-hidden="true"><rect x="0.5" y="0.5" width="11" height="11" rx="2" fill="var(--tagline-blue)"/></svg>
      /lumarove.beauty
    </li>
  </ul>
</section>

<section class="card card--back" aria-label="Business card back">
  <div class="back-logo">
    <div class="brand-name"><span class="brand-dot"></span>Lumarove</div>
    <div class="brand-sub">ACADEMY OF BEAUTY</div>
  </div>
  <h2 class="offerings-title">We Offerings</h2>
  <ul class="program-lines">
    <li>• Cosmetology • Barber • Spa Therapy • Massage Therapy</li>
    <li>• Makeup Artistry • Skin Care • Manicure • Pedicure &amp; Nail Extensions</li>
    <li>• Full Specialist</li>
  </ul>
</section>

</body>
</html>
```